Letterhead for financial advisor-insurance agent firm

Our company, Harlow Pemberton Insurance & Investments, is an insurance (health, life, home, auto, etc) and investment brokerage offering a suite of options to meet client needs. We need letterhead that is professional and embodies strength, security and sophistication.

http://jobs.brieftrove.example/job.aspx?id=518264

Industry/Entity Type

Investment

```html
<!DOCTYPE html>
<html lang="en">
<head>
<meta charset="utf-8">
<title>Harlow Pemberton Letterhead</title>
<link rel="stylesheet" href="https://fonts.googleapis.com/css2?family=Cinzel:wght@600&family=Didact+Gothic&display=swap">
<style>
  :root {
    --backdrop: #d6d4d6;
    --paper: #ffffff;
    --navy: #2d2a4a;
    --steel: #6b7178;
    --footer-text: #ffffff;
  }
  * { margin: 0; padding: 0; box-sizing: border-box; }
  html, body {
    width: 900px;
    height: 1200px;
    overflow: hidden;
    background: var(--backdrop);
  }
  .letterhead {
    position: absolute;
    left: 103px;
    top: 47px;
    width: 708px;
    height: 1000px;
    background: var(--paper);
  }
  .brand {
    position: absolute;
    top: 19px;
    left: 0;
    width: 100%;
    text-align: center;
    color: var(--navy);
    font-family: "Cinzel", serif;
    font-weight: 600;
  }
  .brand-square {
    display: block;
    width: 77px;
    height: 77px;
    margin: 0 auto 11px;
    border: 2.5px solid var(--navy);
  }
  .brand-name {
    display: block;
    font-size: 28px;
    letter-spacing: 0.5px;
    line-height: 1;
  }
  .brand-tagline {
    display: block;
    margin-top: 6px;
    font-size: 11.5px;
    letter-spacing: 0.6px;
    line-height: 1;
  }
  .footer-rule {
    position: absolute;
    left: 0;
    top: 902px;
    width: 100%;
    height: 9px;
    background: var(--steel);
  }
  .footer {
    position: absolute;
    left: 0;
    top: 911px;
    width: 100%;
    height: 89px;
    background: var(--navy);
    padding: 8px 0 0 20px;
  }
  .contact-list { list-style: none; }
  .contact-item {
    display: flex;
    align-items: center;
    gap: 4px;
    height: 17.5px;
    color: var(--footer-text);
    font-family: "Didact Gothic", sans-serif;
    font-size: 15px;
    line-height: 1;
  }
  .contact-icon {
    width: 16px;
    height: 14px;
    fill: none;
    stroke: #d9d9e0;
    stroke-width: 1.4;
  }
</style>
</head>
<body>
  <main class="letterhead">
    <header class="brand">
      <span class="brand-square"></span>
      <span class="brand-name">Harlow Pemberton</span>
      <span class="brand-tagline">Insurance &amp; Investments</span>
    </header>

    <div class="footer-rule"></div>
    <footer class="footer">
      <ul class="contact-list">
        <li class="contact-item">
          <svg class="contact-icon" viewBox="0 0 16 14" aria-hidden="true"><path d="M3 1.5l2.5 2.5-1.5 1.8c.8 1.6 2 2.8 3.7 3.7l1.8-1.5 2.5 2.5-1.5 1.5C6.5 11.5 3 8 1.5 3z"/></svg>
          <span>1742 318 604</span>
        </li>
        <li class="contact-item">
          <svg class="contact-icon" viewBox="0 0 16 14" aria-hidden="true"><rect x="1.5" y="3" width="13" height="9"/><path d="M1.5 3l6.5 5 6.5-5"/></svg>
          <span>info@harlowpemberton.com</span>
        </li>
        <li class="contact-item">
          <svg class="contact-icon" viewBox="0 0 16 14" aria-hidden="true"><circle cx="8" cy="7" r="6"/><ellipse cx="8" cy="7" rx="2.6" ry="6"/><path d="M2 7h12M3 4h10M3 10h10"/></svg>
          <span>www.harlowpemberton.com</span>
        </li>
        <li class="contact-item">
          <svg class="contact-icon" viewBox="0 0 16 14" aria-hidden="true"><path d="M1.5 7.5L8 1.5l6.5 6M3.5 6v6.5h3.5v-4h2v4h3.5V6"/></svg>
          <span>P.O. Box 48207, elm street, riverton</span>
        </li>
      </ul>
    </footer>
  </main>
</body>
</html>
```